Sheriff Candidate needs a large yard sign

A candidate for Sheriff needs to have a sign to put in front of businesses and houses that advertise her candidacy.

Target Market(s)

Democrats, voters

Industry/Entity Type

Political

Font styles to use
Sans Serif

Colors
34a7d7
3276b5

Requirements
Must have
• Must have her picture
• Must have the words "Elect Dana Whitlock" - I'd like the name Dana to be smaller Whitlock. "Elect" and "Whitlock" should be the focus.
• at the bottom in a box "Paid for by the Committee to Elect Dana Whitlock"
Nice to have
• it would be good to have her logo as well.
• blue color for democrats and on a white background
Should not have
• pink color

```html
<!DOCTYPE html>
<html lang="en">
<head>
<meta charset="utf-8">
<title>Elect Dana Whitlock – Yard Sign</title>
<link href="https://fonts.googleapis.com/css2?family=Encode+Sans+Condensed:wght@400;700;800&display=swap" rel="stylesheet">
<style>
  :root {
    --sky-blue: #34a7d7;
    --deep-blue: #3276b5;
    --white: #ffffff;
    --slate: #5b5b5d;
    --photo-dark: #5e5f61;
    --photo-light: #a3a4a6;
  }
  html, body {
    margin: 0;
    padding: 0;
    width: 1200px;
    height: 1000px;
    overflow: hidden;
    background: var(--white);
  }
  .yard-sign {
    display: block;
    width: 1200px;
    height: 1000px;
    font-family: "Encode Sans Condensed", "Arial Narrow", sans-serif;
  }
  .band { fill: var(--sky-blue); }
  .divider-gap { fill: none; stroke: var(--white); stroke-width: 12; }
  .divider-slate { fill: none; stroke: var(--slate); stroke-width: 9; }
  .divider-blue { fill: none; stroke: var(--deep-blue); stroke-width: 5; }
  .rule { stroke: var(--deep-blue); stroke-width: 3; }
  .headline { fill: var(--deep-blue); font-weight: 800; }
  .first-name { fill: var(--sky-blue); font-weight: 400; }
  .campaign-name { fill: var(--deep-blue); font-weight: 700; letter-spacing: 1px; }
  .campaign-dot { fill: var(--white); stroke: var(--sky-blue); stroke-width: 10; }
  .disclaimer-lead { fill: var(--white); font-weight: 400; }
  .disclaimer-name { fill: var(--white); font-weight: 800; }
</style>
</head>
<body>
<svg class="yard-sign" viewBox="0 0 1200 1000" xmlns="http://www.w3.org/2000/svg">
  <defs>
    <linearGradient id="portraitTone" x1="0" y1="0" x2="1" y2="1">
      <stop offset="0" stop-color="var(--photo-light)"/>
      <stop offset="0.55" stop-color="var(--photo-dark)"/>
      <stop offset="1" stop-color="#2a2c33"/>
    </linearGradient>
    <path id="arcEdge" d="M427 0 C600 180 640 560 540 790 C500 880 440 950 367 1000"/>
  </defs>

  <rect class="sign-face" width="1200" height="1000" fill="var(--white)"/>

  <!-- top wave band -->
  <path class="band top-band" d="M420 0 H1200 V122 C1120 120 1040 112 1000 96 C960 40 870 40 830 96 C760 110 660 100 560 92 L480 90 Z"/>

  <!-- bottom disclaimer band -->
  <rect class="band bottom-band" x="380" y="858" width="820" height="142"/>

  <!-- curved dividers -->
  <use href="#arcEdge" class="divider-blue" transform="translate(30 0)"/>
  <use href="#arcEdge" class="divider-slate" transform="translate(17 0)"/>
  <use href="#arcEdge" class="divider-gap" transform="translate(5 0)"/>

  <!-- candidate portrait area -->
  <path class="portrait" role="img" aria-label="Portrait photo of candidate Dana Whitlock in a dark blazer"
        fill="url(#portraitTone)"
        d="M0 0 H427 C600 180 640 560 540 790 C500 880 440 950 367 1000 H0 Z"/>

  <!-- campaign name in place of the logo -->
  <g class="campaign-mark">
    <circle class="campaign-dot" cx="913" cy="190" r="95"/>
    <text class="campaign-name" x="913" y="350" font-size="42" text-anchor="middle">WHITLOCK FOR SHERIFF</text>
  </g>

  <!-- headline -->
  <text class="headline" x="652" y="598" font-size="165" textLength="318" lengthAdjust="spacingAndGlyphs">ELECT</text>

  <g class="name-rules">
    <line class="rule" x1="658" y1="630" x2="790" y2="630"/>
    <line class="rule" x1="658" y1="650" x2="790" y2="650"/>
    <line class="rule" x1="658" y1="670" x2="790" y2="670"/>
    <line class="rule" x1="1010" y1="630" x2="1173" y2="630"/>
    <line class="rule" x1="1010" y1="650" x2="1173" y2="650"/>
    <line class="rule" x1="1010" y1="670" x2="1173" y2="670"/>
  </g>
  <text class="first-name" x="805" y="688" font-size="92" textLength="190" lengthAdjust="spacingAndGlyphs">DANA</text>

  <text class="headline" x="723" y="808" font-size="150" textLength="452" lengthAdjust="spacingAndGlyphs">WHITLOCK</text>

  <!-- disclaimer -->
  <text class="disclaimer-lead" x="546" y="910" font-size="48" textLength="454" lengthAdjust="spacingAndGlyphs">Paid for by the Committee to</text>
  <text class="disclaimer-name" x="546" y="984" font-size="86" textLength="583" lengthAdjust="spacingAndGlyphs">ELECT DANA WHITLOCK</text>
</svg>
</body>
</html>
```